Banner Ad for website hompage - Design Project

We need 4 banner ads for the homepage of a Rent a Car company based in dubai. We rent a wide range of cars but mainly deal in the affordable cars category. Our website colors are mainly red, white and black and I can send pictures of the website (attached) if you want something to compare possible design ideas with. The banners need to promote different messages and must be appealing to the end user. It must also use pictures of cars that exist in our fleet (Pls note: this is only if you are using cars in the banner ad)

The 4 banner ads needed are as follows:
1) should promote something along the lines of we have 20+ models available and reserve a car now (This banner should also have a reserve now button, not the actual button but it's design. The button will be made and coded by us)
2) should promote something along the lines of we offer personalised service and we look after each and every custoemr individually
3) we provide attractive rates based on daily, weekly, monthly and longer rental periods (should also incorporate a reserve now message)
4) Like us on quorvia and follow us on social media for additional offers and discounts (would like for this to have a like button design implemented in it which will be linked to quorvia.)

Also please not the picture file size is 940pixels by 400pixels

Finally: I also need the psd files for the banners.

```html
<!DOCTYPE html>
<html lang="en">
<head>
<meta charset="utf-8">
<title>Rent a Car Banners</title>
<link rel="stylesheet" href="https://fonts.googleapis.com/css2?family=Arimo:wght@400;700&display=swap">
<style>
  :root {
    --red: #e30613;
    --red-dark: #b5000c;
    --grey-text: #6b6b6b;
    --black: #111111;
    --white: #ffffff;
    --panel-light: #ffffff;
    --panel-shade: #dcdcdc;
    --page: #ffffff;
    --like-blue: #2f6fb8;
    --like-fill: #e8f1fb;
  }
  * { margin: 0; padding: 0; box-sizing: border-box; }
  html, body {
    width: 1200px; height: 1061px; overflow: hidden;
    background: var(--page);
    font-family: "Arimo", Arial, sans-serif;
  }
  .canvas { position: relative; width: 1200px; height: 1061px; }
  .banner {
    position: absolute; left: 10px; width: 1180px; height: 505px;
    overflow: hidden;
    background: linear-gradient(180deg, var(--panel-light) 35%, var(--panel-shade) 100%);
  }
  .banner--rates { top: 10px; }
  .banner--social { top: 540px; }
  .banner__art { position: absolute; inset: 0; width: 1180px; height: 505px; }
  .banner__copy {
    position: absolute; left: 620px; width: 560px;
    text-align: center; text-transform: uppercase;
    color: var(--grey-text);
    white-space: nowrap;
  }
  .banner--rates .banner__copy { top: 80px; font-size: 44px; line-height: 45px; }
  .banner--social .banner__copy { top: 137px; font-size: 41px; line-height: 44px; }
  .accent { color: var(--red); font-weight: 700; }
  .strong { color: var(--black); font-weight: 700; }
  .reserve-button {
    position: absolute; left: 662px; top: 363px; width: 450px; height: 82px;
  }
  .reserve-button__label {
    position: absolute; left: 50px; right: 0; top: 5px; height: 69px;
    display: flex; align-items: center; justify-content: center;
    color: var(--white); font-weight: 700; font-size: 40px;
    text-transform: uppercase;
    text-shadow: 1px 2px 2px rgba(0,0,0,0.45);
  }
  .like-pill__text {
    font-family: "Arimo", Arial, sans-serif;
    font-weight: 700; font-size: 19px; fill: var(--like-blue);
  }
</style>
</head>
<body>
<div class="canvas">

  <section class="banner banner--rates">
    <svg class="banner__art" viewBox="0 0 1180 505">
      <defs>
        <linearGradient id="skyline-tone" x1="0" y1="0" x2="0" y2="1">
          <stop offset="0" stop-color="#8fb3c2"/>
          <stop offset="0.55" stop-color="#9aa7ad"/>
          <stop offset="0.8" stop-color="#6f7a80"/>
          <stop offset="1" stop-color="#4d565b"/>
        </linearGradient>
      </defs>
      <polygon points="0,0 589,0 529,505 0,505" fill="url(#skyline-tone)"
               role="img" aria-label="Photo of a city skyline with tall towers and a red car driving on a highway"/>
      <polygon points="589,0 616,0 556,505 529,505" fill="var(--red)"/>
    </svg>
    <div class="banner__copy">
      <span class="accent">Attractive rates</span><br>
      Based on daily,<br>
      weekly, monthly<br>
      and longer<br>
      rental periods
    </div>
    <div class="reserve-button">
      <svg width="450" height="82" viewBox="0 0 450 82">
        <defs>
          <linearGradient id="button-red" x1="0" y1="0" x2="0" y2="1">
            <stop offset="0" stop-color="#f01a22"/>
            <stop offset="1" stop-color="var(--red-dark)"/>
          </linearGradient>
        </defs>
        <polygon points="50,18 80,18 40,78 0,78" fill="#c8c8c8"/>
        <polygon points="70,5 450,5 450,74 33,74" fill="url(#button-red)"/>
        <rect x="60" y="74" width="390" height="6" fill="#d5d5d5"/>
      </svg>
      <div class="reserve-button__label">Reserve now</div>
    </div>
  </section>

  <section class="banner banner--social">
    <svg class="banner__art" viewBox="0 0 1180 505">
      <defs>
        <radialGradient id="hand-tone" cx="0.45" cy="0.6" r="0.7">
          <stop offset="0" stop-color="#c7a892"/>
          <stop offset="0.35" stop-color="#6b7f99"/>
          <stop offset="1" stop-color="#3c4e6c"/>
        </radialGradient>
        <clipPath id="photo-area">
          <polygon points="0,0 589,0 529,505 0,505"/>
        </clipPath>
        <symbol id="like-pill" viewBox="0 0 100 40" overflow="visible">
          <rect x="1" y="1" width="98" height="38" rx="19" fill="var(--like-fill)" stroke="var(--like-blue)" stroke-width="2" opacity="0.92"/>
          <text class="like-pill__text" x="12" y="27">LIKE</text>
          <circle cx="80" cy="20" r="16" fill="var(--like-blue)"/>
        </symbol>
      </defs>
      <polygon points="0,0 589,0 529,505 0,505" fill="url(#hand-tone)"
               role="img" aria-label="Blurred photo of a hand touching floating like buttons"/>
      <g class="like-buttons" clip-path="url(#photo-area)">
        <use href="#like-pill" x="159" y="89" width="257" height="103"/>
        <use href="#like-pill" x="147" y="20" width="81" height="32"/>
        <use href="#like-pill" x="447" y="40" width="113" height="45"/>
        <use href="#like-pill" x="-4" y="70" width="92" height="37"/>
        <use href="#like-pill" x="-6" y="186" width="111" height="44"/>
        <use href="#like-pill" x="372" y="239" width="129" height="52"/>
        <use href="#like-pill" x="504" y="149" width="62" height="25"/>
        <use href="#like-pill" x="140" y="283" width="94" height="38"/>
      </g>
      <polygon points="589,0 616,0 556,505 529,505" fill="var(--red)"/>
    </svg>
    <div class="banner__copy">
      Like us on <span class="accent">quorvia</span><br>
      and follow us on<br>
      <span class="accent">social media</span> for<br>
      additional <span class="strong">offers</span><br>
      and <span class="strong">discounts</span>
    </div>
  </section>

</div>
</body>
</html>
```